Web Design Project - Beachwear Affiliate Website needs an eyedropping look!

Hello,
I need a website design that incorporates a logo design as well for an affiliate site that features beachwear including swimwear, coverups, hats, bags, etc. I want it to have the look and feel of an ecommerce site but without the shopping cart so when the visitor gets to the purchase/buy button, they will be sent to the partner via affiliate link in a new window. This is a site targeting women's beachwear so I'm looking for a soft color palette.
LOGO: Looking for a beautiful text based logo with elegant fonts. The Site Logo should read "Tidelane Outfitters" with possibly some sort of break element between the two words. Possibly two different colors for each word. Please no beach type elements such as sun, umbrella, etc. Just nice and clean.
This requires 4 distinct page levels/designs. All pages should have navigation to the other categories without paging backwards.
Main Page - Large picture window in the top center. I would like this to be a slider rotating various pictures. 4 smaller picture spaces specials or products should be underneath the main picture. One should be designed in the style of the site with a text box reading "Weekly Specials".
Main Menu's for the following product categories: Home, Bikinis, One Piece Swimsuits, Modest Swimwear, Beach Cover Ups, Beach Hats & Bags, Specialty Swimwear, About Sizing) For Menu categories above that require subcategories, I'd like a mouseover effect to show the subcategories so users can bypass the subcategories page through direct navigation. Smaller links in the top right or bottom center for About Us, Contact, & Partners.
Subcategory Page - For Bikinis, Modest Swimwear, and Specialty Swimwear, I need a subcategory page offering image based sub-categories with text. The top of each of these pages should have space for text content. Please use filler text in your designs to get a sense for look. It can say anything or just be jibberish in your example. I will provide the subcategories in a separate uploaded file but as an example, Bikinis will have categories like String Bikinis, Brazilian Bikinis, G-string Bikini's etc. (Note Images should be sized to 200w x 312h pixels)
Category Page - This will be the main image gallery page for each category/subcategory. Images with ability to add pricing text underneath. Two buttons per image: More Info & Purchase. Purchase will take them to an external website utilizing affiliate links in a new window. More Info or clicking on the picture will take you to the product page. (Note images should be sized to 200w x 312h pixels
Product Page - Larger image sized to 420w x 629h with space for a product description to the right along with space to add sizing information as needed. Purchase button will take user to external website utilizing affiliate links in a new window.
Target Market(s)
Women 21-50 searching for Beachwear
Industry/Entity Type
Shopping
Requirements
Must have
- Please see details in the project description. Pages need to be able to be easily SEO'd and incorporate search engine friendly urls.
Simplicity in updating or adding product pages or additional categories is essential.
Social Network Integrated buttons for Quillo, Mingleboard, and Vantora Circle throughout the site.
Nice to have
- I'd really like to integrate a blog posting page so that I can add unique written content for the search engines.
Should not have
- Shopping cart/Ecommerce
Dark Color Palette

```html
<!DOCTYPE html>
<html lang="en">
<head>
<meta charset="utf-8">
<title>Tidelane Outfitters</title>
<link rel="stylesheet" href="https://fonts.googleapis.com/css2?family=Roboto+Condensed:wght@400;700&family=Open+Sans:wght@400;600;700&family=Sacramento&display=swap">
<style>
:root{
  --crimson:#c8003f;
  --ink:#1a1a1a;
  --nav:#2a2a2a;
  --text:#555;
  --rule:#dcdcdc;
  --white:#fff;
  --footer:#000;
}
*{box-sizing:border-box;margin:0;padding:0}
html,body{width:970px;height:1200px;overflow:hidden;background:var(--white);font-family:"Open Sans",Arial,sans-serif}
.page{position:relative;width:970px;height:1200px}
.wrap{position:absolute;left:146px;width:678px}

.site-header{position:absolute;top:0;left:0;width:970px;height:54px}
.brand{position:absolute;left:146px;top:14px;font-family:"Roboto Condensed",sans-serif;font-weight:700;font-size:21px;color:var(--crimson);letter-spacing:-.3px}
.util-nav{position:absolute;right:146px;top:27px;display:flex;font-size:7px;font-weight:600;color:var(--ink);text-transform:uppercase}
.util-nav span{padding:0 9px;border-left:1px solid #333;line-height:8px}
.util-nav span:first-child{border-left:0}
.util-nav span:last-child{padding-right:0}

.main-nav{position:absolute;top:54px;left:0;width:970px;height:36px;background:linear-gradient(#333,#1e1e1e);border-bottom:1px dashed #777}
.main-nav ul{list-style:none;display:flex;justify-content:space-between;position:absolute;left:161px;right:162px;top:12px;color:var(--white);font-size:8.4px;font-weight:600}

.hero{position:absolute;top:90px;left:0;width:970px;height:405px;background:linear-gradient(120deg,#cfc2ad 0%,#a48a70 35%,#8a6e58 55%,#b9a38b 80%,#d8cbb6 100%)}
.hero-arrow{position:absolute;top:178px}
.hero-title{position:absolute;left:149px;top:256px;font-family:"Roboto Condensed",sans-serif;font-weight:700;font-size:46px;color:var(--white);letter-spacing:-1px}
.hero-tagline{position:absolute;left:158px;top:316px;font-family:"Sacramento",cursive;font-size:36px;color:var(--white)}

.section-bar{top:512px;height:35px;background:var(--crimson);color:var(--white);font-family:"Roboto Condensed",sans-serif;font-size:19px;padding:7px 17px}

.card{position:absolute;border-top:3px solid var(--crimson);overflow:hidden}
.card-title{position:absolute;font-family:"Roboto Condensed",sans-serif;color:var(--white);line-height:1}
.card-script{font-family:"Sacramento",cursive}
.buy-btn{position:absolute;background:var(--crimson);color:var(--white);font-family:"Roboto Condensed",sans-serif;font-size:15px;text-align:center}
.card-caption{position:absolute;background:rgba(30,30,30,.85)}

.card-modest{left:146px;top:558px;width:188px;height:329px;background:linear-gradient(160deg,#d9a55a,#8c5a2a 55%,#3a2414)}
.card-hats{left:339px;top:558px;width:237px;height:156px;background:linear-gradient(180deg,#eef2f5,#c9cfd4 60%,#8a8078)}
.card-cover{left:587px;top:558px;width:237px;height:156px;background:linear-gradient(135deg,#6a5a4a,#2f2620 60%,#4a3c30)}
.card-special{left:339px;top:722px;width:485px;height:165px;background:linear-gradient(180deg,#c8d4e2,#8fa6c4 55%,#dfe6ee)}

.blog-head{top:905px;height:42px;border-top:2px solid var(--rule);border-bottom:2px solid var(--rule)}
.blog-head h2{position:absolute;left:8px;top:4px;font-family:"Sacramento",cursive;font-weight:400;font-size:30px;color:var(--ink)}
.pager{position:absolute;right:0;top:12px;display:flex;gap:3px}
.pager span{width:14px;height:14px;background:var(--crimson);display:flex;align-items:center;justify-content:center}
.blog-posts{top:960px;display:flex}
.post{width:180px;padding:0 0 0 2px;border-right:1px dashed var(--rule);height:106px}
.post + .post{padding-left:29px}
.post:nth-child(2),.post:nth-child(3){width:188px}
.post:last-child{border-right:0}
.post h3{font-family:"Roboto Condensed",sans-serif;font-size:9.6px;color:var(--crimson);margin-bottom:5px}
.post p{font-size:7.2px;line-height:12.5px;color:var(--text);text-align:justify;width:128px}
.read-more{display:inline-block;margin-top:8px;background:var(--crimson);color:var(--white);font-family:"Roboto Condensed",sans-serif;font-weight:700;font-size:7px;padding:5px 7px}

.site-footer{position:absolute;left:0;top:1093px;width:970px;height:107px;background:var(--footer);color:var(--white)}
.foot-links{position:absolute;list-style:none;font-size:6.4px;font-weight:600;text-transform:uppercase}
.foot-links li{height:14px}
.foot-main{left:150px;top:16px}
.foot-main li{height:16px}
.foot-cats{left:240px;top:15px}
.newsletter{position:absolute;left:369px;top:29px;width:191px;height:34px;border:2px solid #3c3c3c;background:#1c1c1c;display:flex;align-items:center;padding-left:9px;gap:10px;color:#8a8a8a;font-family:"Roboto Condensed",sans-serif;font-size:14px}
.follow{position:absolute;left:580px;top:32px;display:flex;align-items:center;gap:5px;font-size:6px;color:#777}
.social{width:17px;height:17px;border-radius:2px;background:linear-gradient(#b5b5b5,#6e6e6e)}
.copyright{position:absolute;right:146px;top:30px;text-align:right;font-size:7.6px;line-height:14px;color:#bbb}
.copyright b{font-weight:400;color:#2aa6c8}
</style>
</head>
<body>
<div class="page">

  <header class="site-header">
    <div class="brand">Tidelane Outfitters</div>
    <nav class="util-nav"><span>Home</span><span>About Sizing</span><span>Contact</span><span>My Account</span></nav>
  </header>

  <nav class="main-nav">
    <ul><li>Bikinis</li><li>One Piece Swimsuits</li><li>Modest Swimwear</li><li>Beach Cover Ups</li><li>Beach Hats &amp; Bags</li><li>Specialty Swimwear</li></ul>
  </nav>

  <section class="hero" role="img" aria-label="Slider photo: woman in a pink patterned bikini reclining on pale rocks and pebbles">
    <svg class="hero-arrow" style="left:150px" width="40" height="40" viewBox="0 0 40 40"><circle cx="20" cy="20" r="18" fill="rgba(255,255,255,.15)" stroke="rgba(255,255,255,.7)" stroke-width="2"/><path d="M23 12 L15 20 L23 28" fill="none" stroke="rgba(255,255,255,.8)" stroke-width="3"/></svg>
    <svg class="hero-arrow" style="left:782px" width="40" height="40" viewBox="0 0 40 40"><circle cx="20" cy="20" r="18" fill="rgba(255,255,255,.15)" stroke="rgba(255,255,255,.7)" stroke-width="2"/><path d="M17 12 L25 20 L17 28" fill="none" stroke="rgba(255,255,255,.8)" stroke-width="3"/></svg>
    <div class="hero-title">TIDELANE OUTFITTERS</div>
    <div class="hero-tagline">We will be selling womens beachwear</div>
  </section>

  <div class="wrap section-bar">Weekly Specials</div>

  <article class="card card-modest" role="img" aria-label="Photo: woman in a leopard print bikini on a golden beach">
    <div class="card-caption" style="left:0;top:239px;width:188px;height:90px"></div>
    <div class="card-title" style="left:17px;top:253px;font-size:12.5px">MODEST</div>
    <div class="card-title" style="left:17px;top:266px;font-size:28px">SWIMWEAR</div>
    <div class="buy-btn" style="left:101px;top:298px;width:87px;height:31px;line-height:31px">BUY NOW</div>
  </article>

  <article class="card card-hats" role="img" aria-label="Photo: woman in a brown swimsuit against a pale sky">
    <div class="card-caption" style="left:0;top:100px;width:237px;height:56px"></div>
    <div class="card-title" style="left:11px;top:108px;font-size:16px">BEACH HATS &amp; BAGS</div>
    <div class="card-title card-script" style="left:11px;top:127px;font-size:17px">Lorem Ipsum is simply</div>
    <div class="buy-btn" style="left:149px;top:124px;width:88px;height:32px;line-height:32px">BUY NOW</div>
  </article>

  <article class="card card-cover" role="img" aria-label="Photo: woman in sunglasses lying on wet rocks">
    <div class="card-title" style="left:10px;top:24px;font-size:20px">BEACH COVER UPS</div>
    <div class="buy-btn" style="left:7px;top:48px;width:87px;height:31px;line-height:31px">BUY NOW</div>
  </article>

  <article class="card card-special" role="img" aria-label="Photo: woman in a floral top and flower crown by a harbour">
    <div class="card-title" style="left:19px;top:51px;font-size:26px;color:var(--ink)">SPECIALTY SWIMWEAR</div>
    <div class="card-title card-script" style="left:19px;top:85px;font-size:32px;color:var(--crimson)">Lorem Ipsum is simply dummy</div>
    <div class="buy-btn" style="left:0;top:134px;width:87px;height:31px;line-height:31px">BUY NOW</div>
  </article>

  <div class="wrap blog-head">
    <h2>Our Blog</h2>
    <div class="pager">
      <span><svg width="8" height="8" viewBox="0 0 8 8"><path d="M5.5 1 L2.5 4 L5.5 7" fill="none" stroke="#fff" stroke-width="1.6"/></svg></span>
      <span><svg width="8" height="8" viewBox="0 0 8 8"><path d="M2.5 1 L5.5 4 L2.5 7" fill="none" stroke="#fff" stroke-width="1.6"/></svg></span>
    </div>
  </div>

  <section class="wrap blog-posts">
    <article class="post"><h3>LOREM IPSUM IS SIMPLY DUMMY</h3><p>Lorem Ipsum is simply dummy text of the printing and typesetting industry. Lorem Ipsum has been the industry's standard dummy text ever since the 1500s, when an unknown.</p><span class="read-more">READMORE</span></article>
    <article class="post"><h3>LOREM IPSUM IS SIMPLY DUMMY</h3><p>Lorem Ipsum is simply dummy text of the printing and typesetting industry. Lorem Ipsum has been the industry's standard dummy text ever since the 1500s, when an unknown.</p><span class="read-more">READMORE</span></article>
    <article class="post"><h3>LOREM IPSUM IS SIMPLY DUMMY</h3><p>Lorem Ipsum is simply dummy text of the printing and typesetting industry. Lorem Ipsum has been the industry's standard dummy text ever since the 1500s, when an unknown.</p><span class="read-more">READMORE</span></article>
    <article class="post"><h3>LOREM IPSUM IS SIMPLY DUMMY</h3><p>Lorem Ipsum is simply dummy text of the printing and typesetting industry. Lorem Ipsum has been the industry's standard dummy text ever since the 1500s, when an unknown.</p><span class="read-more">READMORE</span></article>
  </section>

  <footer class="site-footer">
    <ul class="foot-links foot-main"><li>Home</li><li>About Sizing</li><li>Contact</li></ul>
    <ul class="foot-links foot-cats"><li>Bikinis</li><li>One Piece Swimsuits</li><li>Modest Swimwear</li><li>Beach Cover Ups</li><li>Beach Hats &amp; Bags</li><li>Specialty Swimwear</li></ul>
    <div class="newsletter">
      <svg width="28" height="18" viewBox="0 0 28 18"><rect x="1" y="1" width="26" height="16" fill="none" stroke="#8a8a8a" stroke-width="2"/><path d="M1 1 L14 10 L27 1" fill="none" stroke="#8a8a8a" stroke-width="2"/></svg>
      SIGN UP FOR NEWSLETTER
    </div>
    <div class="follow">FOLLOW US :
      <span class="social" aria-label="Mingleboard"></span>
      <span class="social" aria-label="Quillo"></span>
      <span class="social" aria-label="Vantora Circle"></span>
    </div>
    <div class="copyright">Copyright © 2013<br><b>Harborlane Studio.</b> All Rights Reserved.</div>
  </footer>

</div>
</body>
</html>
```